C.L.P. - Need Postcard & Business Card & Coupons

I'm looking for 2 sided postcards (177.8mm x 127mm) and 2 sided Business Card (88.9mm x 50.8mm). These are to promote my website that I sell online printing (crispleafprint.com). I'm only looking for 1 design to use on all items so they all look alike. I attached my logo and sample designs my local designer did that I don't like. All the info is on the sample. I'm looking for flashier designs with lots of color and with photos to catch your eye. Not sure if the photos should be of the type of items we sell or of flashy backgrounds or both. These cards will be left at stores on their counters in the local area and we want people to pick them up from the counter and know what they are for right away with out having to read the whole card to figure it out.
Target Market(s)
People who buy online printing.
Industry/Entity Type
Printing

```html
<!DOCTYPE html>
<html lang="en">
<head>
<meta charset="utf-8">
<title>Crisp Leaf Printing – Business Card</title>
<link href="https://fonts.googleapis.com/css2?family=Open+Sans:ital,wght@0,400;0,600;0,700;1,700&display=swap" rel="stylesheet">
<style>
  :root{
    --cyan:#29abe2;
    --magenta:#e6068a;
    --yellow:#fcea1b;
    --ink:#1c1c1c;
    --pale-pink:#f2aecb;
    --pale-blue:#b3d6f1;
    --pale-yellow:#fbf1b3;
    --paper:#ffffff;
    --backdrop:#ebe7e2;
  }
  *{margin:0;padding:0;box-sizing:border-box}
  html,body{width:1200px;height:1000px;overflow:hidden;background:var(--backdrop)}
  body{position:relative;font-family:"Open Sans",Arial,sans-serif;color:var(--ink)}

  .card{position:absolute;left:220px;width:760px;height:434px;overflow:hidden;background:var(--paper);box-shadow:0 6px 18px rgba(0,0,0,.18)}
  .card--back{top:44px}
  .card--front{top:522px}

  .card__artwork{position:absolute}
  .card--back .card__artwork{
    inset:0;
    background:linear-gradient(100deg,var(--cyan) 0%,var(--cyan) 28%,var(--magenta) 48%,var(--magenta) 58%,var(--yellow) 78%,var(--yellow) 100%);
  }
  .card--front .card__artwork{
    left:380px;top:0;right:0;bottom:0;
    background:
      linear-gradient(180deg,rgba(255,255,255,0) 55%,var(--pale-blue) 100%),
      linear-gradient(90deg,var(--pale-pink) 0%,#fbe3ee 45%,var(--pale-yellow) 100%);
    opacity:.85;
  }

  .brand{position:absolute;display:flex;align-items:center;gap:14px;font-weight:600;color:var(--ink);white-space:nowrap}
  .brand__dot{border-radius:50%;flex:none}
  .card--back .brand{left:50%;top:50%;transform:translate(-50%,-50%);font-size:48px}
  .card--back .brand__dot{width:34px;height:34px;background:var(--paper)}
  .card--front .brand{right:40px;top:62px;font-size:26px}
  .card--front .brand__dot{width:22px;height:22px;background:var(--magenta)}

  .person{position:absolute;left:60px;top:112px}
  .person__name{font-size:44px;font-weight:600;line-height:1.05}
  .person__name .first{color:var(--cyan)}
  .person__name .last{color:var(--magenta)}
  .person__title{font-size:24px;font-weight:700;font-style:italic;color:#e9d60e;margin-top:2px}

  .contact{position:absolute;left:44px;top:232px;list-style:none;font-size:22px;line-height:1.2}
  .contact li{display:flex;align-items:flex-start;gap:10px;margin-bottom:4px}
  .contact svg{width:24px;height:24px;flex:none;margin-top:2px}
</style>
</head>
<body>

<section class="card card--back" aria-label="Business card, back">
  <div class="card__artwork" role="img" aria-label="Flowing cyan, magenta and yellow ink splash artwork"></div>
  <div class="brand"><span class="brand__dot"></span>Crisp Leaf Printing</div>
</section>

<section class="card card--front" aria-label="Business card, front">
  <div class="card__artwork" role="img" aria-label="Faded pink, yellow and blue ink splash artwork"></div>

  <div class="brand"><span class="brand__dot"></span>Crisp Leaf Printing</div>

  <div class="person">
    <p class="person__name"><span class="first">Name</span> <span class="last">Name</span></p>
    <p class="person__title">Designation</p>
  </div>

  <ul class="contact">
    <li>
      <svg viewBox="0 0 24 24" aria-hidden="true"><circle cx="12" cy="12" r="12" fill="var(--cyan)"/><path d="M6 12.5 12 7l6 5.5h-2V18h-3v-3.5h-2V18H8v-5.5Z" fill="#fff"/></svg>
      <span>48 Harlow Lane<br>Brookfield, NY 11590</span>
    </li>
    <li>
      <svg viewBox="0 0 24 24" aria-hidden="true"><circle cx="12" cy="12" r="12" fill="var(--magenta)"/><path d="M8 6h3l1 3-2 1.5a8 8 0 0 0 3.5 3.5L15 12l3 1v3c-6 1-11-4-10-10Z" fill="#fff"/></svg>
      <span>555 014 2261</span>
    </li>
    <li>
      <svg viewBox="0 0 24 24" aria-hidden="true"><circle cx="12" cy="12" r="12" fill="#f3dc10"/><rect x="7" y="6" width="10" height="5" fill="#fff"/><rect x="6" y="11" width="12" height="6" rx="1" fill="#fff"/></svg>
      <span>555 014 2278</span>
    </li>
    <li>
      <svg viewBox="0 0 24 24" aria-hidden="true"><circle cx="12" cy="12" r="12" fill="var(--cyan)"/><rect x="6" y="8" width="12" height="8" fill="#fff"/><path d="M6 8l6 5 6-5" fill="none" stroke="var(--cyan)" stroke-width="1.2"/></svg>
      <span>info@crispleafprint.com</span>
    </li>
    <li>
      <svg viewBox="0 0 24 24" aria-hidden="true"><circle cx="12" cy="12" r="12" fill="var(--magenta)"/><circle cx="12" cy="12" r="6" fill="none" stroke="#fff" stroke-width="1.5"/><path d="M6 12h12M12 6c-3 3-3 9 0 12M12 6c3 3 3 9 0 12" fill="none" stroke="#fff" stroke-width="1.2"/></svg>
      <span>www.crispleafprint.com</span>
    </li>
  </ul>
</section>

</body>
</html>
```